Brightmere Commercial Cleaning - Company OverView

I require a 3 page, A4 company folding proschure. I would like to convey a eco frienddly and professional service. Text and images can be found on our company web page www.brightmerecleaning.com.au however we may need some more eco friendly images to convey the right message

The broschure must highlight our companys ISO certification. We are a professional service targeting the corporate industry.

I have hi res images to send and also endorsement and certification logos to send through.

Designer may need to suppl;y some contact and images.

We would like to work with someoe frquently
Updates

HI TEAM, I AM SORRY FOR ANY CONFUSION. I HAVE JUST HAD INSTRUCTIONS THAT THE BROSCHURE WILL NEED TO BE AN A3 SIZE BUT DESIGNED WITH 2 A4 PAGES FRONT AND BACK. SORRY FOR ANY INCONVENIENCE

Target Market(s)

* Corporate
* Professional

Industry/Entity Type

Professional Service

Requirements
Must have
• * Environmental Feel
* Strong Prescense
* Must be CLEAN
* Have 6 A4 pages (Must be a 3 page a4 broschure, Double sided).
Should not have
• * Busy Text
* Old Font

```html
<!DOCTYPE html>
<html lang="en">
<head>
<meta charset="utf-8">
<title>Brightmere Commercial Cleaning – Company Overview</title>
<link href="https://fonts.googleapis.com/css2?family=Cormorant+Garamond:wght@400;500&family=Questrial&display=swap" rel="stylesheet">
<style>
  :root {
    --navy: #2c4270;
    --navy-deep: #1f2f52;
    --green: #3f8f2f;
    --text: #4a5566;
    --panel: #94b3cc;
    --panel-text: #3e4a5c;
    --white: #ffffff;
    --rule: #8fa08a;
    --badge-red: #c8484f;
    --badge-grey: #b9c2b4;
  }
  * { margin: 0; padding: 0; box-sizing: border-box; }
  html, body { width: 1200px; height: 848px; overflow: hidden; background: var(--white); }
  body { font-family: "Questrial", Arial, sans-serif; color: var(--text); }
  .spread { position: relative; width: 1200px; height: 848px; overflow: hidden; }
  .brand { color: var(--green); }

  .photo { position: absolute; }
  .photo--boardroom { left: 0; top: 0; width: 598px; height: 150px;
    background: linear-gradient(180deg, #7fa7d6 0%, #c9dcef 55%, #9aa3ad 75%, #4b5058 100%); }
  .photo--office { left: 598px; top: 0; width: 602px; height: 150px;
    background: linear-gradient(100deg, #c9935f 0%, #e8d3b5 40%, #bcc6cf 70%, #4b7fb8 100%); }
  .photo--walkway { left: 601px; top: 688px; width: 599px; height: 160px;
    background: radial-gradient(ellipse at 55% 30%, #d9e6f3 0%, #6f8fb2 35%, #1e2f4a 80%); }

  .curves { position: absolute; left: 0; top: 0; }
  .curves--walkway { left: 601px; top: 680px; }

  .heading { position: absolute; font-family: "Cormorant Garamond", Georgia, serif; font-weight: 500;
    color: var(--navy); text-align: center; font-size: 24px; line-height: 26px; }
  .heading--intro { left: 100px; width: 400px; top: 145px; }
  .heading--manage { left: 640px; width: 500px; top: 145px; }

  .copy { position: absolute; font-size: 11px; line-height: 16.6px; letter-spacing: -0.1px; }
  .copy p + p { margin-top: 15px; }
  .copy--intro { left: 57px; top: 214px; width: 478px; }
  .copy--col { top: 216px; width: 220px; text-align: justify; line-height: 15.2px; font-size: 10.6px; letter-spacing: -0.15px; }
  .copy--col p + p { margin-top: 5px; }
  .copy--col-a { left: 651px; }
  .copy--col-b { left: 916px; }
  .col-rule { position: absolute; left: 891px; top: 214px; width: 1px; height: 110px; background: #9aa4b0; }

  .badge { position: absolute; }
  .badge--award { left: 57px; top: 424px; width: 96px; height: 32px; border-radius: 3px; background: var(--badge-red); opacity: .8; }
  .badge--cert { left: 474px; top: 408px; width: 62px; height: 62px; border-radius: 50%; background: var(--badge-grey); }

  .services-title { position: absolute; left: 651px; top: 347px; width: 484px; display: flex; align-items: center;
    gap: 6px; color: var(--green); font-size: 14px; }
  .services-title::before, .services-title::after { content: ""; flex: 1; height: 1px; background: var(--rule); }
  .services-title::before { flex: 0 0 206px; }

  .list { position: absolute; list-style: none; font-size: 11px; letter-spacing: -0.1px; }
  .list li { position: relative; padding-left: 16px; }
  .list li::before { content: ""; position: absolute; left: 0; top: 4px; width: 7px; height: 7px; background: var(--green); }
  .list--services { top: 366px; line-height: 18.7px; }
  .list--services-a { left: 681px; }
  .list--services-b { left: 957px; }

  .panel { position: absolute; top: 486px; height: 362px; background: var(--panel); }
  .panel--values { left: 0; width: 597px; }
  .panel--safety { left: 601px; width: 599px; }
  .divider { position: absolute; left: 597px; top: 486px; width: 4px; height: 362px; background: var(--navy); }
  .top-band { position: absolute; left: 0; top: 483px; width: 1200px; height: 4px; background: var(--navy); }

  .integrity { position: absolute; left: 161px; top: 488px; width: 274px; height: 78px;
    background: linear-gradient(180deg, #3b4a6a 0%, #25324d 100%); display: flex; align-items: center; justify-content: center;
    font-family: "Cormorant Garamond", Georgia, serif; font-size: 40px; letter-spacing: 5px; color: #e4e9f1; }
  .tag { position: absolute; height: 30px; background: var(--navy); border: 1px solid #c9d6e4;
    font-family: "Cormorant Garamond", Georgia, serif; color: #dfe7f1; font-size: 23px; text-align: center; line-height: 28px; }
  .tag--solid { left: 188px; top: 575px; width: 222px; }
  .tag--ohs { left: 836px; top: 490px; width: 118px; height: 37px; line-height: 36px; font-size: 24px; border: none; background: #3e5176; }

  .list--values { left: 78px; top: 619px; line-height: 19.8px; color: var(--panel-text); }
  .list--values li { padding-left: 17px; }

  .copy--safety { left: 651px; top: 535px; width: 482px; color: var(--panel-text); line-height: 16.8px; }
  .copy--safety p + p { margin-top: 8px; }
</style>
</head>
<body>
<main class="spread">
  <div class="photo photo--boardroom" role="img" aria-label="Boardroom table with black leather chairs against a bright sky"></div>
  <div class="photo photo--office" role="img" aria-label="Clean modern office corridor with white chairs and blue glass"></div>

  <svg class="curves" width="1200" height="160" viewBox="0 0 1200 160" aria-hidden="true">
    <path d="M0 160 L0 152 Q300 112 598 140 Q900 112 1200 140 L1200 160 Z" fill="var(--white)"/>
    <path d="M0 152 Q300 112 598 140" fill="none" stroke="var(--navy)" stroke-width="4"/>
    <path d="M598 140 Q900 112 1200 140" fill="none" stroke="var(--navy)" stroke-width="4"/>
  </svg>

  <h1 class="heading heading--intro">A new generation dedicated<br>to customer service</h1>
  <div class="copy copy--intro">
    <p>Established in 1995 and initially servicing commercial and strata offices, <span class="brand">Brightmere</span> has progressively developed over 15 years to build a strong client network thought Australia and New Zealand.</p>
    <p><span class="brand">Brightmere</span> now offers the highest commercial cleaning standards to commercial industry, retail and shopping centres, hotels and tertiary education facilities.</p>
    <p>Our continual commitment and dedication to delivering a quality service has enabled <span class="brand">Brightmere</span> to build a solid foundation and international presence.</p>
    <p>Building relationships based on ethical conduct towards employees and clientele defines our unique working environments and is a vital key to our success.</p>
  </div>
  <div class="badge badge--award" aria-hidden="true"></div>
  <div class="badge badge--cert" aria-hidden="true"></div>

  <h2 class="heading heading--manage"><span class="brand">Brightmere</span>. Making the management of your<br>property easier and cleaner</h2>
  <div class="copy copy--col copy--col-a">
    <p><span class="brand">Brightmere</span> is considered one of Australia’s leading Commercial Cleaning service provider, dedicated to delivering a quality service that adds value.</p>
    <p><span class="brand">Brightmere’s</span> commitment to deliver quality is reflected in our rapidly growing clientele base and long term working relationships.</p>
  </div>
  <div class="col-rule"></div>
  <div class="copy copy--col copy--col-b">
    <p><span class="brand">Brightmere</span> has built a process orientated service with measurable quality control methods and procedures based on accountability.</p>
    <p><span class="brand">Brightmere</span> delivers a wide range of quality services, ensuring that the management of your site is handled with competence and reliability.</p>
  </div>

  <div class="services-title">Services</div>
  <ul class="list list--services list--services-a">
    <li>General cleaning requirements</li>
    <li>Security – 24 hour emergency contact</li>
    <li>Consumables supply and replacement</li>
    <li>Wash room services</li>
    <li>Building maintenance</li>
    <li>Scrubbing machinery</li>
  </ul>
  <ul class="list list--services list--services-b">
    <li>Pressure washing</li>
    <li>Window cleaning</li>
    <li>Carpet care</li>
    <li>Floor maintenance</li>
    <li>Graffiti removal</li>
  </ul>

  <section class="panel panel--values"></section>
  <section class="panel panel--safety"></section>
  <div class="top-band"></div>
  <div class="divider"></div>

  <div class="photo photo--walkway" role="img" aria-label="Long illuminated moving walkway in a blue-lit tunnel"></div>
  <svg class="curves curves--walkway" width="599" height="40" viewBox="0 0 599 40" aria-hidden="true">
    <path d="M0 0 L599 0 L599 8 Q300 22 0 4 Z" fill="var(--panel)"/>
    <path d="M0 4 Q300 22 599 8" fill="none" stroke="var(--navy)" stroke-width="3"/>
  </svg>

  <div class="integrity">INTEGRITY</div>
  <div class="tag tag--solid">Or it could be solid</div>
  <ul class="list list--values">
    <li>Our principle to put the client first, separates us from the rest</li>
    <li>Engrained within each employee are five company principles of <span class="brand">Brightmere</span>.</li>
    <li>Put the client first</li>
    <li>Lead with integrity</li>
    <li>Deliver a quality service</li>
    <li>Take personal responsibility</li>
    <li>Keep &nbsp;balance</li>
    <li>Within these principles <span class="brand">Brightmere</span> has created a company that rewards dependability,<br>integrity, safety and provides the training and development for all employees.</li>
  </ul>

  <div class="tag tag--ohs">OH&amp;S</div>
  <div class="copy copy--safety">
    <p><span class="brand">Brightmere</span> is certified to the ISO Occupational Health and Safety Standard AS/NZ 4801/2001</p>
    <p>There can be no greater responsibility to our employees and clients than that of the safety and quality in which commercial and industrial cleaning services are conducted. <span class="brand">Brightmere</span> takes a proactive approach to the management, training and development of our OH&amp;S systems, responsibilities and obligations.</p>
    <p>In the process of building and managing a solid and safe environment, <span class="brand">Brightmere</span> works closely with the governing association Safeline Authority and is an active member of the Facility Services Contractors Guild FSCG.</p>
  </div>
</main>
</body>
</html>
```